New modern website for Kerbline Groundworks

Hi we are an existing company that has a current website http://www.kerblinegroundworks.co.nz/ we are looking to get a new vibrant looking website designed to take us further and gain more customers. We are after a simple easy to use website that does not confuse but we want to make an impact and stand out from the rest

Target Market(s)

Homeowners And Commercial Businesses

Industry/Entity Type

It Company

Coding

Coded - Design and coding required

Number of Pages Required

2 page

```html
<!DOCTYPE html>
<html lang="en">
<head>
<meta charset="utf-8">
<title>Kerbline Groundworks – Concrete &amp; Asphalt Paving Auckland</title>
<link rel="stylesheet" href="https://fonts.googleapis.com/css2?family=Roboto:wght@300;400;500;700&display=swap">
<style>
:root{
  --yellow:#f2cf00;
  --yellow-deep:#f5b400;
  --black:#0d0d0d;
  --ink:#1a1a1a;
  --paper:#e2e2e2;
  --bubble:#6d6d6d;
  --rule:#9a9a9a;
  --white:#ffffff;
  --muted:#666666;
}
*{margin:0;padding:0;box-sizing:border-box}
html,body{width:1200px;height:2616px;overflow:hidden}
body{position:relative;background:var(--paper);font-family:"Roboto",Arial,sans-serif;color:var(--ink)}
.abs{position:absolute}

/* header */
.site-header{left:0;top:0;width:1200px;height:93px;background:var(--white)}
.brand{left:99px;top:26px;display:flex;align-items:center;gap:12px;font-weight:700;font-size:29px;color:var(--black);letter-spacing:.5px}
.brand-mark{width:18px;height:18px;background:var(--black)}
.contact-strip{left:851px;top:13px;height:27px;display:flex}
.contact-phone{width:117px;background:var(--black);color:var(--white);font-size:13px;font-weight:700;display:flex;align-items:center;justify-content:center}
.contact-quote{width:134px;background:var(--yellow-deep);color:var(--black);font-size:12px;font-weight:500;display:flex;align-items:center;padding-left:14px;clip-path:polygon(0 0,90% 0,100% 50%,90% 100%,0 100%)}
.main-nav{top:52px;left:643px;display:flex;font-size:13px}
.main-nav a{color:var(--black);text-decoration:none;height:27px;display:flex;align-items:center;padding:0 16px;margin-right:10px}
.main-nav a.is-active{border:1px solid var(--black)}

/* hero */
.hero{left:0;top:93px;width:1200px;height:531px;background:linear-gradient(100deg,#5c6a5a 0%,#7b8078 35%,#4a4b46 60%,#8a7a30 78%,#3a3a36 100%)}
.hero-title{left:99px;top:258px;font-size:40px;line-height:44px;font-weight:400;color:var(--white)}
.hero-title strong{display:block;color:var(--yellow);font-weight:500}
.hazard-band{left:0;top:624px;width:1200px;height:8px;background:repeating-linear-gradient(90deg,var(--yellow) 0 14px,transparent 14px 22px)}

/* intro */
.intro-heading{left:0;top:688px;width:1200px;text-align:center;font-size:34px;font-weight:300;line-height:44px}
.intro-heading strong{display:block;font-weight:500;font-size:32px}
.feature{top:837px;width:330px;text-align:center}
.feature-icon{height:150px;display:flex;align-items:center;justify-content:center}
.feature-seal{width:152px;height:152px;border-radius:50%;background:var(--black)}
.feature-pictogram{width:120px;height:110px;background:linear-gradient(var(--black) 0 75%,var(--yellow) 75%)}
.feature-pictogram.is-road{width:96px;height:100px;background:linear-gradient(var(--black) 0 40%,var(--yellow) 40% 58%,var(--black) 58%)}
.feature h3{font-size:16px;font-weight:500;margin-top:22px}
.feature p{font-size:12px;line-height:15.5px;margin:12px auto 0;width:255px}
.feature-divider{top:820px;width:1px;height:279px;background:#bdbdbd}
.dash-rule{height:4px;background:repeating-linear-gradient(90deg,var(--black) 0 12px,transparent 12px 20px)}

/* cards */
.promo-card{top:1238px;width:489px;height:258px;overflow:hidden}
.promo-card .photo{position:absolute;inset:0}
.promo-card .shade{position:absolute;left:0;right:0;bottom:0;height:150px;background:linear-gradient(transparent,rgba(0,0,0,.9) 60%)}
.promo-card h2{position:absolute;left:25px;top:150px;font-size:34px;font-weight:400;color:var(--white);padding-bottom:4px;border-bottom:3px solid var(--yellow)}
.promo-card p{position:absolute;left:25px;top:212px;font-size:16px;color:var(--white)}

/* section headings */
.section-heading{left:99px;width:1003px;display:flex;align-items:center;gap:18px;font-size:24px;font-weight:400;color:var(--ink)}
.section-heading::before,.section-heading::after{content:"";flex:1;height:1px;background:var(--rule);box-shadow:0 3px 0 var(--rule)}

/* testimonials */
.testimonial{top:1669px;width:317px}
.testimonial blockquote{position:relative;background:var(--bubble);color:#f2f2f2;border-radius:6px;padding:22px 24px 22px 30px;font-size:13px;line-height:20px;height:166px}
.testimonial blockquote p+p{margin-top:20px}
.testimonial blockquote::after{content:"";position:absolute;right:20px;bottom:-20px;border-left:20px solid transparent;border-top:20px solid var(--bubble)}
.quote-mark{position:absolute;font-size:40px;color:#9c9c9c;line-height:1}
.quote-close{color:#9c9c9c;font-size:26px}
.author{display:flex;align-items:center;gap:10px;margin:12px 0 0 155px}
.avatar{width:34px;height:34px;border-radius:50%;background:linear-gradient(#b9a89a,#6b5f57)}
.author b{display:block;font-size:13px;font-weight:500}
.author span{font-size:10px}

/* gallery */
.gallery-sub{left:0;top:2030px;width:1200px;text-align:center;font-size:15px;color:var(--muted)}
.gallery-item{top:2084px;width:231px;height:145px}

/* call to action */
.cta{left:99px;top:2288px;width:1003px;height:136px;background:var(--white)}
.cta-dark{position:absolute;left:0;top:0;width:540px;height:136px;background:var(--black);clip-path:polygon(0 0,100% 0,90% 100%,0 100%)}
.cta-dark p{position:absolute;left:35px;top:30px;color:var(--white);font-size:24px;font-weight:300}
.cta-dark strong{position:absolute;left:35px;top:64px;color:var(--yellow-deep);font-size:38px;font-weight:700}
.cta-numbers{position:absolute;left:558px;top:14px;font-size:41px;font-weight:700;line-height:52px;color:var(--black)}

/* footer */
.site-footer{left:0;top:2529px;width:1200px;height:87px;background:var(--black)}
.footer-nav{position:absolute;left:99px;top:24px;display:flex;gap:36px;font-size:12px}
.footer-nav a{color:#8a8a8a;text-decoration:none}
.copyright{position:absolute;left:99px;top:50px;font-size:10px;color:#4d4d4d}
.social{position:absolute;left:908px;top:21px;display:flex;gap:30px}
.social span{width:44px;height:44px;border-radius:50%;border:2px solid #3b73b8}
</style>
</head>
<body>

<header class="site-header abs">
  <div class="brand abs"><span class="brand-mark"></span>Kerbline Groundworks</div>
  <div class="contact-strip abs">
    <span class="contact-phone">09 555 0142</span>
    <span class="contact-quote">REQUEST QUOTE</span>
  </div>
  <nav class="main-nav abs">
    <a class="is-active" href="#">HOME</a><a href="#">ABOUT</a><a href="#">SERVICES</a><a href="#">PROJECTS</a><a href="#">CONTACT US</a>
  </nav>
</header>

<section class="hero abs" role="img" aria-label="Photo of a yellow asphalt truck spraying bitumen onto a gravel road"></section>
<h1 class="hero-title abs">Setting the standards for<strong>Concrete and Asphalters</strong></h1>
<div class="hazard-band abs"></div>

<svg class="abs" style="left:0;top:0" width="1200" height="2616" aria-hidden="true">
  <g fill="var(--yellow)">
    <rect x="0" y="659" width="35" height="361"/>
    <rect x="61" y="659" width="40" height="361"/>
    <rect x="1099" y="816" width="40" height="361"/>
    <rect x="1160" y="816" width="40" height="361"/>
    <polygon points="1102,1430 1102,1480 1200,1640 1200,1580"/>
    <polygon points="1040,1496 1090,1496 1200,1680 1200,1740"/>
    <polygon points="0,1831 0,1890 80,1990 80,1930"/>
    <polygon points="0,1925 0,1985 80,2085 80,2025"/>
  </g>
</svg>

<h2 class="intro-heading abs">The trusted name for all<strong>Concrete &amp; Asphalt Paving in Auckland</strong></h2>

<div class="feature abs" style="left:97px">
  <div class="feature-icon"><span class="feature-seal" role="img" aria-label="Experience badge"></span></div>
  <h3>Years of Experience</h3>
  <p>We have a reputation with clients in and around Auckland for achieving great results on time and within budget every time. We are proud to share our years of experience.</p>
</div>
<div class="feature-divider abs" style="left:427px"></div>
<div class="feature abs" style="left:430px">
  <div class="feature-icon"><span class="feature-pictogram" role="img" aria-label="Icon of a house with a paved driveway"></span></div>
  <h3>Concreting &amp; Asphalt Work</h3>
  <p>When it comes to all asphalt services, you can rest assured we will work around your schedule, requirements and budget. Servicing throughout Auckland, we specialise in.</p>
</div>
<div class="feature-divider abs" style="left:760px"></div>
<div class="feature abs" style="left:761px">
  <div class="feature-icon"><span class="feature-pictogram is-road" role="img" aria-label="Icon of a road with a yellow barrier"></span></div>
  <h3>Additional Services</h3>
  <p>As part of our asphalt services, we are proud to offer a range of related services to our clients in the eastern suburbs and greater Auckland. Specialising in residential, commercial and industrial projects.</p>
</div>

<div class="dash-rule abs" style="left:0;top:1174px;width:1064px"></div>

<article class="promo-card abs" style="left:99px">
  <div class="photo" role="img" aria-label="Photo of a road crew laying asphalt beside a tipper truck" style="background:linear-gradient(160deg,#9aa3a8,#6b6a55 55%,#3a3a30)"></div>
  <div class="shade"></div>
  <h2>Services</h2>
  <p>Complete asphalt services for your next</p>
</article>
<article class="promo-card abs" style="left:612px">
  <div class="photo" role="img" aria-label="Photo of a finished residential asphalt driveway with garden" style="background:linear-gradient(160deg,#6d8a52,#4a5a3c 50%,#2d2d2a)"></div>
  <div class="shade"></div>
  <h2>Projects</h2>
  <p>For residential driveways and commercial</p>
</article>

<div class="dash-rule abs" style="left:99px;top:1550px;width:942px"></div>

<h2 class="section-heading abs" style="top:1610px">Customer Testimonials</h2>

<figure class="testimonial abs" style="left:99px">
  <blockquote><span class="quote-mark" style="left:8px;top:12px">“</span><p>Lorem ipsum dolor sit amet, consectetur adipiscing elit, sed do eiusmod tempor incididunt ut labore et dolore magna aliqua.</p><p>Sed ut perspiciatis unde omnis iste natus error sit voluptatem accusantium <span class="quote-close">”</span></p></blockquote>
  <figcaption class="author"><span class="avatar"></span><span><b>Mark Tanner</b><span>CEO, Example Co</span></span></figcaption>
</figure>
<figure class="testimonial abs" style="left:443px">
  <blockquote><span class="quote-mark" style="left:8px;top:12px">“</span><p>Lorem ipsum dolor sit amet, consectetur adipiscing elit, sed do eiusmod tempor incididunt ut labore et dolore magna aliqua.</p><p>Sed ut perspiciatis unde omnis iste natus error sit voluptatem accusantium <span class="quote-close">”</span></p></blockquote>
  <figcaption class="author"><span class="avatar"></span><span><b>Mark Tanner</b><span>CEO, Example Co</span></span></figcaption>
</figure>
<figure class="testimonial abs" style="left:785px">
  <blockquote><span class="quote-mark" style="left:8px;top:12px">“</span><p>Lorem ipsum dolor sit amet, consectetur adipiscing elit, sed do eiusmod tempor incididunt ut labore et dolore magna aliqua.</p><p>Sed ut perspiciatis unde omnis iste natus error sit voluptatem accusantium <span class="quote-close">”</span></p></blockquote>
  <figcaption class="author"><span class="avatar"></span><span><b>Mark Tanner</b><span>CEO, Example Co</span></span></figcaption>
</figure>

<h2 class="section-heading abs" style="top:1984px">Our Project Gallery</h2>
<p class="gallery-sub abs">For residential driveways and commercial paving in Auckland</p>
<div class="gallery-item abs" style="left:99px;background:linear-gradient(#c9cfd4,#8e9294)" role="img" aria-label="Photo of workers finishing a concrete slab"></div>
<div class="gallery-item abs" style="left:356px;background:linear-gradient(#b7c4cf,#6e6d66)" role="img" aria-label="Photo of a freshly sealed commercial yard"></div>
<div class="gallery-item abs" style="left:614px;background:linear-gradient(#5d7a45,#3e3f3b)" role="img" aria-label="Photo of a garden-lined residential driveway"></div>
<div class="gallery-item abs" style="left:870px;background:linear-gradient(90deg,#c9a27a,#2f2f33)" role="img" aria-label="Photo of an asphalt path beside a timber fence"></div>

<section class="cta abs">
  <div class="cta-dark">
    <p>Any Questions you would like to ask?</p>
    <strong>Need to talk to us...</strong>
  </div>
  <div class="cta-numbers">Mobile : 027 555 0199<br>PHONE :09 55 50 142</div>
</section>

<footer class="site-footer abs">
  <nav class="footer-nav"><a href="#">HOME</a><a href="#">ABOUT</a><a href="#">SERVICES</a><a href="#">PROJECTS</a><a href="#">CONTACT US</a></nav>
  <p class="copyright">©2016 . All rights reserved</p>
  <div class="social" aria-label="Social links"><span></span><span></span><span></span></div>
</footer>

</body>
</html>
```